Dryer Vent Cleaning Postcard Design

We need a postcard design for Flue Wranglers, a company that specializes in dryer vent cleaning, repairs and upgrades. Dryer vents need periodic cleaning to avoid lint clogging, dryer malfunction, long dry times and even a house fire. This card will be sent to residential and businesses prospects to introduce them to our services and the importance of maintaining their dryer vents. Our website is @ fluewrangling.com and provides information about our services, photos of our work and our general color scheme (purple/orange). Final print size will be 5x7 horizontal.

Target Market(s)

homeowners and business owners (spas, salons, grooming, gyms, laundrymats, etc)

Requirements
Must have
• Reduce the risk of fire
shortened dry times
lower energy consumption
18000 dryer fires caused in the US per year
Nice to have
• Does your dryer take too long to dry?

```html
<!DOCTYPE html>
<html lang="en">
<head>
<meta charset="utf-8">
<title>Flue Wranglers – Dryer Vent Cleaning Postcard</title>
<link rel="stylesheet" href="https://fonts.googleapis.com/css2?family=Source+Sans+3:wght@600;700&display=swap">
<style>
  :root {
    --purple: #45386d;
    --orange: #f4834a;
    --white: #ffffff;
    --sky: #7a9bd0;
    --ring: #ee5a35;
  }
  * { margin: 0; padding: 0; box-sizing: border-box; }
  html, body { width: 857px; height: 1200px; overflow: hidden; background: var(--white); }
  .postcard {
    position: relative;
    width: 857px;
    height: 1200px;
    font-family: "Source Sans 3", "Myriad Pro", sans-serif;
    overflow: hidden;
    background: var(--white);
  }
  .backdrop { position: absolute; inset: 0; }
  .line {
    position: absolute;
    left: 0;
    width: 100%;
    text-align: center;
    white-space: nowrap;
  }
  .headline {
    color: var(--orange);
    font-weight: 700;
    font-size: 72px;
    line-height: 1;
    letter-spacing: -1px;
  }
  .headline-1 { top: 66px; }
  .headline-2 { top: 154px; }
  .benefit {
    color: var(--white);
    font-weight: 600;
    font-size: 45px;
    line-height: 1;
    letter-spacing: -0.5px;
  }
  .benefit .dot {
    display: inline-block;
    width: 12px;
    height: 12px;
    border-radius: 50%;
    background: var(--orange);
    margin-right: 12px;
    vertical-align: middle;
    position: relative;
    top: -3px;
  }
  .benefit-1 { top: 271px; }
  .benefit-2 { top: 347px; }
  .benefit-3 { top: 422px; }
  .benefit-4 { top: 497px; }
  .benefit-4b { top: 548px; }
  .mascot-area {
    position: absolute;
    left: 298px;
    top: 660px;
    width: 262px;
    height: 262px;
    border-radius: 50%;
    background: radial-gradient(circle at 50% 40%, var(--sky) 0%, #5c6fa8 70%, var(--ring) 71%, var(--orange) 100%);
  }
  .brand-name {
    top: 912px;
    color: var(--purple);
    font-weight: 700;
    font-size: 40px;
    line-height: 1;
  }
  .call {
    top: 972px;
    color: var(--orange);
    font-weight: 700;
    font-size: 62px;
    line-height: 1;
    letter-spacing: -1px;
  }
  .phone {
    top: 1042px;
    color: var(--orange);
    font-weight: 700;
    font-size: 66px;
    line-height: 1;
    letter-spacing: -1px;
  }
  .contact {
    top: 1128px;
    color: var(--purple);
    font-weight: 700;
    font-size: 29px;
    line-height: 1;
  }
  .contact .divider { color: var(--orange); padding: 0 6px; }
</style>
</head>
<body>
<main class="postcard">
  <svg class="backdrop" width="857" height="1200" viewBox="0 0 857 1200" aria-hidden="true">
    <path d="M0 0 H857 V714 Q428.5 555 0 714 Z" fill="var(--purple)"/>
  </svg>

  <h1 class="line headline headline-1">Does your dryer</h1>
  <p class="line headline headline-2">take too long to dry?</p>

  <ul class="benefits">
    <li class="line benefit benefit-1"><span class="dot"></span>Reduce the risk of fire</li>
    <li class="line benefit benefit-2"><span class="dot"></span>Shortened dry times</li>
    <li class="line benefit benefit-3"><span class="dot"></span>Lower energy consumption</li>
    <li class="line benefit benefit-4"><span class="dot"></span>18000 dryer fires caused in</li>
  </ul>
  <p class="line benefit benefit-4b">the US per year</p>

  <div class="mascot-area" role="img" aria-label="Illustrated technician with a vent-cleaning brush and backpack vacuum hose, set in a round blue and orange emblem"></div>
  <p class="line brand-name">Flue Wranglers</p>

  <p class="line call">Call Now!</p>
  <p class="line phone">336-555-0142</p>
  <p class="line contact">office@fluewrangling.com<span class="divider">|</span>fluewrangling.com</p>
</main>
</body>
</html>
```